IT Professional Services Marketing Web Site

The Kovrel Associates new web site, need to look clean and modern, it has to give the feel of a professional IT consulting firm (something like white / clean background), the design need to be influenced by this site: http://www.trundavio.com/ .
The whole site is a one page, plus a link to a blog site, with the following sections:
1. Menu
2. Main Area
3. Our Company
4. What we do
5. Our Clients
6. Our People
7. Events
8. Contact Us
The new web site will be hosted on WordPress
Updates

Target Market(s)

Project Management Offices in Medium to Large Organisations

Industry/Entity Type

It Company

Number of Pages Required

1 page

Font styles to use
Serif
Sans Serif

Requirements
Must have
• Implemented on WordPress
Nice to have
• Shadows on the images and areas to give the site a bit of depth

```html
<!DOCTYPE html>
<html lang="en">
<head>
<meta charset="utf-8">
<title>Kovrel Associates – Trusted PMO Partners</title>
<link rel="stylesheet" href="https://fonts.googleapis.com/css2?family=Lato:ital,wght@0,300;0,400;0,700;0,900;1,400&display=swap">
<style>
:root{
  --blue:#1a9ad6;
  --blue-dark:#1585bb;
  --orange:#f7931e;
  --orange-dark:#e07f0c;
  --ink:#4a4a4a;
  --muted:#8a8a8a;
  --light:#f1f1f1;
  --line:#d6d6d6;
  --dark:#3a3a3a;
  --footer:#2b2b2b;
  --white:#ffffff;
}
*{box-sizing:border-box;margin:0;padding:0}
html,body{width:1200px;height:5085px;overflow:hidden}
body{font-family:"Lato",Arial,sans-serif;color:var(--ink);background:var(--white);position:relative}
section,header,footer{position:absolute;left:0;width:1200px}
.abs{position:absolute}
.ph{position:absolute;border-radius:6px}

/* header */
.site-header{top:0;height:120px;background:var(--white);box-shadow:0 2px 6px rgba(0,0,0,.08);z-index:2}
.brand{left:140px;top:26px;display:flex;align-items:center;gap:12px}
.brand-mark{width:34px;height:34px;border-radius:50%;background:var(--orange)}
.brand-name{font-size:34px;font-weight:700;color:var(--muted);letter-spacing:.5px}
.main-nav{right:140px;top:74px;display:flex;gap:20px;font-size:13px;color:var(--muted);text-transform:uppercase}

/* hero */
.hero{top:120px;height:470px;background:linear-gradient(180deg,#e9e9e9,#d9d9d9)}
.hero h1{left:140px;top:130px;font-size:60px;line-height:64px;font-weight:400;color:var(--blue);letter-spacing:1px}
.hero .tagline{left:140px;top:270px;font-size:20px;font-style:italic;color:var(--muted);width:440px;line-height:28px}
.hero .tagline b{font-style:normal;color:var(--ink)}
.hero-arrow{top:200px;font-size:60px;color:var(--muted);font-weight:300}

/* intro */
.intro{top:590px;height:160px;background:var(--white)}
.intro p{position:absolute;left:180px;width:840px;top:28px;text-align:center;font-size:13px;line-height:20px;color:var(--muted)}

/* diagram */
.approach{top:750px;height:1250px;background:linear-gradient(180deg,#ebebeb,#f6f6f6 50%,#e6e6e6)}
.node{position:absolute;border-radius:50%;display:flex;align-items:center;justify-content:center;font-size:16px;font-weight:700;color:var(--ink)}
.node.cloud{background:#a9d9f1;color:var(--blue-dark);border:4px solid var(--white)}
.node.consult{background:#cfcfcf}
.node.care{background:#fbd3a1;color:#a35a05}
.approach p{position:absolute;width:340px;font-size:13px;line-height:21px;color:var(--muted)}

/* services */
.services{top:2000px;height:410px;background:linear-gradient(180deg,#5a5a5a,#3f3f3f)}
.section-title{position:absolute;left:0;width:1200px;text-align:center;font-size:32px;font-weight:400;letter-spacing:1px}
.services .section-title{top:30px;color:var(--white)}
.title-rule{position:absolute;left:520px;width:160px;height:1px;background:currentColor;opacity:.5}
.service{position:absolute;top:130px;width:200px;text-align:center}
.service .ring{width:150px;height:150px;margin:0 auto;border-radius:50%;border:4px solid;display:flex;align-items:center;justify-content:center}
.service .label{margin-top:18px;font-size:30px;color:var(--white);text-transform:uppercase}
.service.cloud .label{background:var(--blue);border-radius:30px;padding:2px 0;width:150px;margin-left:25px}

/* cloud panel */
.service-detail{top:2410px;height:345px;background:var(--blue)}
.service-detail h2{position:absolute;left:450px;top:62px;width:600px;font-size:34px;font-weight:300;line-height:42px;color:var(--white)}
.service-detail p{position:absolute;left:450px;top:160px;width:600px;font-size:13px;line-height:20px;color:#dff1fb}
.btn{display:inline-block;font-size:13px;font-weight:700;text-transform:uppercase;color:var(--white);background:var(--orange);padding:8px 18px;border-radius:2px}
.service-detail .btn{position:absolute;left:450px;top:270px}

/* testimonials */
.love{top:2755px;height:450px;background:var(--white)}
.love .section-title{top:36px;color:var(--orange);font-size:32px}
.tile{position:absolute;padding:16px 18px;color:var(--white);font-size:15px;line-height:20px;overflow:hidden}
.tile.blue{background:var(--blue)}
.tile.orange{background:var(--orange)}
.tile .q{font-size:40px;line-height:20px;vertical-align:-14px;font-weight:900;opacity:.8;margin-right:4px}

/* people */
.people{top:3205px;height:475px;background:var(--white);border-top:1px solid var(--line)}
.people .section-title{top:36px;color:var(--ink)}
.person{position:absolute;top:120px;width:300px;text-align:center}
.avatar{width:130px;height:130px;border-radius:50%;margin:0 auto;border:5px solid var(--white);box-shadow:0 3px 10px rgba(0,0,0,.25);background:linear-gradient(160deg,#bfc4c9,#6f757b)}
.person h3{margin-top:16px;font-size:24px;color:var(--blue);font-weight:700}
.person .role{font-size:15px;font-weight:700;color:var(--ink);margin-top:4px}
.person p{margin:12px auto 0;width:260px;font-size:13px;line-height:19px;color:var(--muted)}
.dots{position:absolute;top:430px;left:560px;display:flex;gap:8px}
.dots i{width:12px;height:12px;border-radius:50%;border:1px solid #aaa;display:block}
.dots i.on{background:#aaa}

/* offices */
.offices{top:3680px;height:640px;background:linear-gradient(135deg,#5e5e5e,#474747)}
.card{position:absolute;background:var(--orange);color:var(--white);border-radius:8px;box-shadow:0 6px 16px rgba(0,0,0,.35)}
.offices-card{left:135px;top:45px;width:380px;height:530px;padding:26px 30px}
.offices-card h2{font-size:32px;font-weight:400;margin-bottom:18px}
.office{font-size:14px;line-height:20px;margin-bottom:16px}
.office b{display:block;font-size:15px}
.office .row{display:flex}
.office .row span:first-child{width:64px;font-weight:700}
.contact-card{left:775px;top:100px;width:285px;height:380px;padding:16px 18px}
.contact-card h2{font-size:30px;font-weight:400;margin-bottom:14px}
.field{background:#fbc27f;border-radius:3px;color:var(--white);font-size:14px;padding:10px 12px;margin-bottom:12px}
.field.msg{height:110px}
.submit{background:#7a3b03;color:var(--white);text-align:center;font-weight:700;font-size:14px;padding:11px;border-radius:3px}

/* events */
.events{top:4320px;height:345px;background:var(--white)}
.event{position:absolute;left:220px;width:840px;height:85px;border-bottom:1px solid var(--line)}
.event .date{font-size:13px;color:var(--muted);font-style:italic}
.event .date b{font-style:normal;color:var(--ink)}
.event h3{font-size:28px;font-weight:700;color:var(--blue);margin-top:4px}
.event h3.alt{color:#6d6d6d}
.rsvp{position:absolute;right:0;top:22px;border:1px solid var(--line);font-size:12px;padding:8px 20px;color:var(--muted)}

/* newsletter */
.newsletter{top:4665px;height:115px;background:var(--light)}
.at{left:135px;top:18px;width:80px;height:80px;border-radius:50%;background:#bdbdbd;color:var(--white);font-size:54px;font-weight:700;display:flex;align-items:center;justify-content:center}
.newsletter h2{position:absolute;left:232px;top:28px;font-size:22px;font-weight:700;letter-spacing:.3px;color:var(--orange);white-space:nowrap}
.newsletter p{position:absolute;left:232px;top:60px;width:370px;font-size:12px;line-height:16px;color:var(--muted)}
.email{left:640px;top:36px;width:275px;height:46px;background:var(--white);border:1px solid var(--line);font-size:13px;color:#aaa;padding:14px}
.send{left:935px;top:36px;width:110px;height:46px;background:var(--white);border:1px solid var(--line);font-size:14px;color:var(--muted);display:flex;align-items:center;justify-content:center}

/* footer */
.site-footer{top:4780px;height:305px;background:var(--footer);color:#bbb}
.cols{position:absolute;left:140px;top:24px;display:flex}
.col{width:155px;font-size:13px;line-height:22px}
.col h4{color:var(--orange);font-size:17px;font-weight:400;margin-bottom:8px}
.social{display:flex;align-items:center;gap:10px;margin-bottom:14px;color:var(--white)}
.social i{width:36px;height:36px;border-radius:50%;background:var(--white);display:block;flex:none}
.copyright{position:absolute;left:0;bottom:0;width:1200px;height:34px;line-height:34px;text-align:center;font-size:12px;background:#1d1d1d;color:#aaa}
</style>
</head>
<body>

<header class="site-header">
  <div class="abs brand"><span class="brand-name">Kovrel Associates</span><span class="brand-mark"></span></div>
  <nav class="abs main-nav">
    <span>Our Company</span><span>What we do</span><span>Our Clients</span><span>Our People</span><span>Events</span><span>Blog</span><span>Contact Us</span>
  </nav>
</header>

<section class="hero">
  <span class="abs hero-arrow" style="left:40px">‹</span>
  <span class="abs hero-arrow" style="right:40px">›</span>
  <h1 class="abs">TRUSTED PMO<br>PARTNERS</h1>
  <div class="abs tagline">Smarter PPM (Project Portfolio Management) Tools, Powered by <b>Nortvale</b></div>
  <div class="ph" role="img" aria-label="Word cloud of project management terms above connected team member icons" style="left:600px;top:60px;width:500px;height:360px;background:radial-gradient(ellipse at center,#ffffff 0%,#f2f2f2 55%,rgba(230,230,230,0) 75%)"></div>
</section>

<section class="intro">
  <p>“Kovrel Associates is a specialist consulting company that focuses solely on the design, configuration, deployment, user training and support of Enterprise Project Management (EPM) solutions based upon Nortvale Plan Server and its supporting technologies.<br>Kovrel Associates offers a true end-to-end set of services for any organisation implementing an EPM solution within their business – to cover the lifecycle of that system.</p>
</section>

<section class="approach" id="what-we-do">
  <svg class="abs" style="left:0;top:0" width="1200" height="1250" viewBox="0 0 1200 1250" aria-hidden="true">
    <path d="M600 0 C600 150 560 220 560 330 C560 400 420 420 400 480 C380 560 680 700 690 860 C700 980 600 1100 600 1250" fill="none" stroke="#c4c4c4" stroke-width="2"/>
  </svg>
  <p style="left:200px;top:50px">Lorem ipsum dolor sit amet, consectetuer adipiscing elit, sed diam nonummy nibh euismod tincidunt ut laoreet dolore magna aliquam erat volutpat. Ut wisi enim ad minim veniam, quis nostrud exerci tation ullamcorper suscipit lobortis nisl ut aliquip ex ea commodo consequat. Duis autem vel eum iriure dolor in hendrerit in vulputate velit esse molestie consequat, vel illum dolore eu feugiat nulla facilisis at vero eros et accumsan et iusto odio dignissim qui blandit praesent luptatum zzril delenit augue duis dolore te feugait nulla facilisi.</p>
  <div class="ph" role="img" aria-label="Cloud software product tiles floating above two boxed server packages" style="left:640px;top:60px;width:420px;height:260px;background:linear-gradient(180deg,#fafafa,#e2e2e2)"></div>
  <div class="node cloud" style="left:510px;top:280px;width:100px;height:100px">CLOUD</div>
  <div class="node consult" style="left:345px;top:425px;width:110px;height:110px">CONSULT</div>
  <div class="ph" role="img" aria-label="Office building beside a group of consultants" style="left:220px;top:560px;width:240px;height:150px;background:linear-gradient(180deg,#6b6b6b,#3e3e3e)"></div>
  <p style="left:620px;top:470px">Lorem ipsum dolor sit amet, consectetuer adipiscing elit, sed diam nonummy nibh euismod tincidunt ut laoreet dolore magna aliquam erat volutpat. Ut wisi enim ad minim veniam, quis nostrud exerci tation ullamcorper suscipit lobortis nisl ut aliquip ex ea commodo consequat. Duis autem vel eum iriure dolor in hendrerit in vulputate velit esse molestie consequat, vel illum dolore eu feugiat nulla facilisis at vero eros et accumsan et iusto odio dignissim qui blandit praesent luptatum zzril delenit augue duis dolore te feugait nulla facilisi. Nam liber tempor cum soluta nobis eleifend option congue nihil imperdiet doming id quod mazim placerat facer possim assum.</p>
  <div class="node care" style="left:635px;top:800px;width:110px;height:110px">CARE</div>
  <p style="left:200px;top:920px">Lorem ipsum dolor sit amet, consectetuer adipiscing elit, sed diam nonummy nibh euismod tincidunt ut laoreet dolore magna aliquam erat volutpat. Ut wisi enim ad minim veniam, quis nostrud exerci tation ullamcorper suscipit lobortis nisl ut aliquip ex ea commodo consequat. Duis autem vel eum iriure dolor in hendrerit in vulputate velit esse molestie consequat, vel illum dolore eu feugiat nulla facilisis at vero eros et accumsan et iusto odio dignissim qui blandit praesent luptatum zzril delenit augue duis dolore te feugait nulla facilisi.</p>
  <div class="ph" role="img" aria-label="Support agent with headset in front of a team silhouette" style="left:680px;top:880px;width:360px;height:300px;background:radial-gradient(circle at center,#5a5a5a 0%,#9a9a9a 40%,rgba(220,220,220,0) 70%)"></div>
</section>

<section class="services">
  <h2 class="section-title">OUR SERVICES</h2>
  <span class="title-rule" style="top:82px;color:#fff"></span>
  <div class="service cloud" style="left:175px">
    <div class="ring" style="border-color:var(--blue);background:rgba(26,154,214,.15)">
      <svg width="84" height="56" viewBox="0 0 84 56" aria-hidden="true"><path d="M20 50 a16 16 0 0 1 2-32 a22 22 0 0 1 41 4 a14 14 0 0 1 1 28 z" fill="none" stroke="#1a9ad6" stroke-width="5"/></svg>
    </div>
    <div class="label">Cloud</div>
  </div>
  <div class="service" style="left:500px">
    <div class="ring" style="border-color:#bdbdbd">
      <svg width="70" height="64" viewBox="0 0 70 64" aria-hidden="true"><path d="M35 6 C16 6 5 17 5 30 c0 8 4 14 11 19 l-4 12 l15-8 c3 1 5 1 8 1 c19 0 30-11 30-24 S54 6 35 6z" fill="none" stroke="#bdbdbd" stroke-width="5" stroke-linejoin="round"/></svg>
    </div>
    <div class="label">Consult</div>
  </div>
  <div class="service" style="left:825px">
    <div class="ring" style="border-color:var(--orange)">
      <svg width="70" height="70" viewBox="0 0 70 70" aria-hidden="true"><path d="M48 8 a14 14 0 0 0-16 18 L8 50 a6 6 0 0 0 10 10 l24-24 a14 14 0 0 0 18-16 l-8 8 l-8-2 l-2-8 z" fill="#f7931e"/></svg>
    </div>
    <div class="label">Care</div>
  </div>
</section>

<section class="service-detail">
  <svg class="abs" style="left:155px;top:70px" width="240" height="160" viewBox="0 0 240 160" aria-hidden="true"><path d="M60 145 a45 45 0 0 1 4-90 a62 62 0 0 1 116 12 a40 40 0 0 1 2 78 z" fill="none" stroke="#0f5f87" stroke-width="10"/></svg>
  <h2>Lorem ipsum dolor sit amet, consectetuer adipiscing elit</h2>
  <p>Lorem ipsum dolor sit amet, consectetuer adipiscing elit, sed diam nonummy nibh euismod tincidunt ut laoreet dolore magna aliquam erat volutpat. Ut wisi enim ad minim veniam, quis nostrud exerci tation ullamcorper suscipit lobortis nisl ut aliquip ex ea commodo consequat. Duis autem vel eum iriure dolor in hendrerit in vulputate velit esse molestie consequat, vel illum dolore eu feugiat nulla facilisis at vero eros et accumsan et iusto odio dignissim qui blandit praesent luptatum zzril delenit augue.</p>
  <span class="btn">Read more →</span>
</section>

<section class="love" id="our-clients">
  <h2 class="section-title">PMOS AROUND AUSTRALIA SHARE THE LOVE</h2>
  <span class="title-rule" style="top:90px;color:var(--orange)"></span>
  <div class="ph" role="img" aria-label="Client office building exterior" style="left:150px;top:130px;width:245px;height:130px;border-radius:0;background:linear-gradient(180deg,#8fb6d4,#3d5f7a)"></div>
  <div class="tile blue" style="left:405px;top:130px;width:130px;height:130px"><span class="q">“</span>Lorem ipsum dolor sit amet, consectetuer adipiscing</div>
  <div class="tile orange" style="left:545px;top:130px;width:245px;height:130px"><span class="q">“</span>Lorem ipsum dolor sit amet, consectetuer adipiscing elit, sed diam nonummy nibh euismod</div>
  <div class="ph" role="img" aria-label="Portrait of a client" style="left:800px;top:130px;width:120px;height:130px;border-radius:0;background:linear-gradient(160deg,#e5e5e5,#b8b8b8)"></div>
  <div class="tile blue" style="left:930px;top:130px;width:120px;height:130px"><span class="q">“</span>Lorem ipsum dolor sit amet, consectetuer</div>
  <div class="tile orange" style="left:150px;top:270px;width:245px;height:130px"><span class="q">“</span>Lorem ipsum dolor sit amet, consectetuer adipiscing elit, sed</div>
  <div class="tile blue" style="left:405px;top:270px;width:130px;height:130px"><span class="q">“</span>Lorem ipsum dolor sit amet, consectetuer</div>
  <div class="ph" role="img" aria-label="Portrait of a client" style="left:545px;top:270px;width:120px;height:130px;border-radius:0;background:linear-gradient(160deg,#e5e5e5,#b8b8b8)"></div>
  <div class="tile blue" style="left:675px;top:270px;width:115px;height:130px"><span class="q">“</span>Lorem ipsum dolor sit amet</div>
  <div class="tile blue" style="left:800px;top:270px;width:250px;height:130px"><span class="q">“</span>Lorem ipsum dolor sit amet, consectetuer adipiscing elit, sed diam nonummy nibh euismod</div>
</section>

<section class="people" id="our-people">
  <h2 class="section-title">OUR PEOPLE</h2>
  <span class="title-rule" style="top:90px;color:var(--ink)"></span>
  <div class="person" style="left:150px"><div class="avatar" role="img" aria-label="Portrait of Aldo Pemberton"></div><h3>Aldo Pemberton</h3><div class="role">President, CEO</div><p>Lorem ipsum dolor sit amet, consectetuer adipiscing elit, sed diam nonummy nibh euismod tincidunt ut</p></div>
  <div class="person" style="left:450px"><div class="avatar" role="img" aria-label="Portrait of Reid Calloway"></div><h3>Reid Calloway</h3><div class="role">Project Manager</div><p>Lorem ipsum dolor sit amet, consectetuer adipiscing elit, sed diam nonummy nibh euismod tincidunt ut</p></div>
  <div class="person" style="left:750px"><div class="avatar" role="img" aria-label="Portrait of Tomas Virelli"></div><h3>Tomas Virelli</h3><div class="role">Project Lead</div><p>Lorem ipsum dolor sit amet, consectetuer adipiscing elit, sed diam nonummy nibh euismod tincidunt ut</p></div>
  <div class="dots"><i class="on"></i><i></i><i></i><i></i></div>
</section>

<section class="offices" id="contact-us">
  <div class="ph" role="img" aria-label="Street map of central Sydney" style="left:0;top:0;width:1200px;height:640px;border-radius:0;background:linear-gradient(135deg,#6a6a6a,#4b4b4b 60%,#555)"></div>
  <svg class="abs" style="left:586px;top:300px" width="28" height="40" viewBox="0 0 28 40" aria-hidden="true"><path d="M14 0 a14 14 0 0 1 14 14 c0 10-14 26-14 26 S0 24 0 14 A14 14 0 0 1 14 0z" fill="#f7931e"/><circle cx="14" cy="14" r="5" fill="#fff"/></svg>
  <div class="card offices-card">
    <h2>OFFICES</h2>
    <div class="office"><b>Kovrel Associates Head Office</b>Suite 210, Level 2,<br>Harbourline House, 14 Merton St<br>Sydney, NSW, 2000<div class="row"><span>Phone:</span><span>02 8000 4417</span></div><div class="row"><span>Fax:</span><span>02 8000 4418</span></div></div>
    <div class="office"><b>Kovrel Associates VIC Office</b>41 Carrow St<br>South Melbourne VIC 3205<div class="row"><span>Phone:</span><span>03 9000 2216</span></div></div>
    <div class="office"><b>Kovrel Associates ACT Office</b>Tower B, Level 4, 9 Lakeview Circuit,<br>Canberra, ACT, 2601<div class="row"><span>Phone:</span><span>02 6000 3381</span></div><div class="row"><span>Fax:</span><span>02 6000 3382</span></div></div>
  </div>
  <div class="card contact-card">
    <h2>CONTACT US</h2>
    <div class="field">Name</div>
    <div class="field">Email</div>
    <div class="field msg">Message</div>
    <div class="submit">SUBMIT</div>
  </div>
</section>

<section class="events" id="events">
  <div class="event" style="top:40px"><div class="date">Next Event: <b>Wednesday 18th March, 2015</b> 2015-3-9 4PM</div><h3>SKYFRAME USERGROUP MEETUP-SYDNEY</h3><span class="rsvp">RSVP</span></div>
  <div class="event" style="top:140px"><div class="date">Next Event: <b>Wednesday 18th March, 2015</b> 2015-3-9 4PM</div><h3 class="alt">USERGROUP MEETUP- ADELAIDE</h3><span class="rsvp">RSVP</span></div>
  <div class="event" style="top:240px;border-bottom:0"><div class="date">Next Event: <b>Wednesday 18th March, 2015</b> 2015-3-9 4PM</div><h3>SUITE 365 USERGROUP MEETUP-SYDNEY</h3><span class="rsvp">RSVP</span></div>
</section>

<section class="newsletter">
  <div class="abs at">@</div>
  <h2>SUBSCRIBE TO OUR NEWSLETTER</h2>
  <p>All the latest updates and event news from our team, delivered to you once a month, with no spam ever.</p>
  <div class="abs email">Enter Your Email Address</div>
  <div class="abs send">SEND</div>
</section>

<footer class="site-footer">
  <div class="cols">
    <div class="col"><h4>Quick Links</h4>Home<br>What We Do<br>Our Clients<br>Our People<br>Events<br>Blog<br>Contact Us</div>
    <div class="col"><h4>Packages</h4>Lorem Ipsum Dolor<br>Consectetuer Adipi<br>Sed Diam Nonummy<br>Euismod Tincidunt Ut<br>Dolore Magna Aliqu<br>Volutpat Ut Wisi<br>Minim Veniam, Quis</div>
    <div class="col"><h4>Schemes</h4>Lorem Ipsum Dolor<br>Consectetuer Adipi<br>Sed Diam Nonummy<br>Euismod Tincidunt Ut<br>Dolore Magna Aliqu<br>Volutpat Ut Wisi<br>Minim Veniam, Quis</div>
    <div class="col"><h4>Services</h4>Lorem Ipsum Dolor<br>Consectetuer Adipi<br>Sed Diam Nonummy<br>Euismod Tincidunt Ut<br>Dolore Magna Aliqu<br>Volutpat Ut Wisi<br>Minim Veniam, Quis</div>
    <div class="col"><h4>Cloud</h4>Lorem Ipsum Dolor<br>Consectetuer Adipi<br>Sed Diam Nonummy<br>Euismod Tincidunt Ut<br>Dolore Magna Aliqu<br>Volutpat Ut Wisi<br>Minim Veniam, Quis</div>
    <div class="col"><h4>Connect With Us</h4>
      <div class="social"><i></i>Community</div>
      <div class="social"><i></i>Video Channel</div>
      <div class="social"><i></i>Updates</div>
    </div>
  </div>
  <div class="copyright">Copyright 2015 Kovrel Associates | All Rights Reserved.</div>
</footer>

</body>
</html>
```